BOND WITH TOBY FOR SPECIALISED ADHESIVE AND SEALANTS.

Details for my new Banner Ad Design Project will be added soon.
All that I am looking for is WORDING that can demonstrate to potential customers what the products can achieve and describing the various materials that this special adhesive will stick and why they need to choose it also a logo or even new name to fit in if financially possible
The size of the banner is unimportant as I only need help in getting the message over then I will adjust accordingly or pay the designer to complete.
As I am very limited in my knowledge of web design in fact it is non existent your help is paramount for the result.
This is a new project for me as I am now a young retired person who is looking for something different to follow.
Please let me know if the information I supply is in sufficient,
Best regards to all and in your design careers.
Updates

As pointed out to me that my request is to broad for a result,but I am not looking for words that describe a space shot, I am looking for suggestions to help me to put together some form of ad that helps me get the business off the ground ,I am no expert in marketing and design, so any format of words would be helpful,thank you all and remember, " you are the experts".

Target Market(s)

General public in the UK,and commercial business.
It would be used where there is a requirement to seal/or stick difficult materials or items but not large items like roofs/buildings etc.

Industry/Entity Type

Adhesive

Font styles to use
Sans Serif

Colors

Designer to choose colors to be used in the design.

Requirements
Must have
• To make people feel they will need the product or service maybe not initially but soon.
Nice to have
• This can be anything related to sticking or sealing different household products,
Should not have
• old fashioned font

```html
<!DOCTYPE html>
<html lang="en">
<head>
<meta charset="utf-8">
<title>Gripwell Adhesive Banner</title>
<link href="https://fonts.googleapis.com/css2?family=Anton&family=Mulish:wght@400&display=swap" rel="stylesheet">
<style>
  :root {
    --paper: #ffffff;
    --ink: #231f20;
    --mark-green: #2f8a4c;
  }
  html, body {
    margin: 0;
    padding: 0;
    overflow: hidden;
    background: var(--paper);
  }
  .banner {
    position: relative;
    width: 1200px;
    height: 335px;
    background: var(--paper);
    overflow: hidden;
  }
  .brand-dot {
    position: absolute;
    left: 226px;
    top: 14px;
    width: 100px;
    height: 100px;
  }
  .brand-name {
    position: absolute;
    left: 126px;
    top: 96px;
    margin: 0;
    font-family: "Anton", "Arial Narrow", sans-serif;
    font-weight: 400;
    font-size: 98px;
    line-height: 96px;
    letter-spacing: 1px;
    color: var(--ink);
    text-transform: uppercase;
  }
  .brand-name span { display: block; }
  .benefits {
    position: absolute;
    left: 600px;
    top: 40px;
    width: 466px;
    margin: 0;
    padding: 0;
    list-style: none;
    text-align: center;
    font-family: "Mulish", "Avenir", sans-serif;
    font-size: 16px;
    line-height: 23px;
    color: var(--ink);
  }
  .benefit { margin: 0 0 20px; }
  .benefit-title {
    display: block;
    text-transform: uppercase;
    letter-spacing: 0.3px;
  }
  .benefit-text { display: block; }
</style>
</head>
<body>
  <main class="banner">
    <svg class="brand-dot" viewBox="0 0 100 100" aria-hidden="true">
      <circle cx="50" cy="50" r="50" fill="var(--mark-green)"/>
    </svg>
    <h1 class="brand-name"><span>Gripwell</span><span>Adhesive</span></h1>

    <ul class="benefits">
      <li class="benefit">
        <span class="benefit-title">Waterproof</span>
        <span class="benefit-text">withstands damp conditions</span>
      </li>
      <li class="benefit">
        <span class="benefit-title">Flexible</span>
        <span class="benefit-text">wide variety of uses</span>
        <span class="benefit-text">sticks almost everything to almost anything</span>
      </li>
      <li class="benefit">
        <span class="benefit-title">Temperature Resistant</span>
        <span class="benefit-text">extremes of temperature will not release bond</span>
      </li>
      <li class="benefit">
        <span class="benefit-title">Easy Finishing</span>
        <span class="benefit-text">sandable product that accepts paint or stain</span>
      </li>
    </ul>
  </main>
</body>
</html>
```